Bref créative
Valcourt Chiropractic
Business card, letterhead, envelope
Professional
Valcourt Chiropractic (use logo)
41785 Brookhaven Rd
Oakridge Twp, MI 48193
info@ValcourtChiroExample.com
www.ValcourtChiroExample.com
Want a design that portrays health and wellness in a professional manner
(in bullet format)
-We Specialize in Improving Health & Wellness Naturally
-Most Insurances Accepted
-Holistic Family Health Care
-Massage Therapist on Staff

```html
<!DOCTYPE html>
<html lang="en">
<head>
<meta charset="utf-8">
<title>Valcourt Chiropractic – Stationery</title>
<link href="https://fonts.googleapis.com/css2?family=Lato:wght@400;700&display=swap" rel="stylesheet">
<style>
  :root{
    --backdrop:#2b2c2e;
    --paper:#ffffff;
    --green:#6b9b3a;
    --green-light:#8ab85a;
    --blue:#1f3f8f;
    --ink:#4a4a4a;
    --muted:#9a9a9a;
    --faint:#eef2ea;
    --fold:#e2e2e2;
  }
  *{box-sizing:border-box;margin:0;padding:0}
  html,body{width:1200px;height:310px;overflow:hidden;background:var(--backdrop)}
  body{position:relative;font-family:"Lato",Arial,sans-serif;color:var(--ink)}
  .piece{position:absolute;background:var(--paper);overflow:hidden;box-shadow:0 2px 6px rgba(0,0,0,.45)}

  /* plain footer stripes */
  .footer-bands{position:absolute;left:0;right:0;bottom:0;display:flex;flex-direction:column}
  .footer-bands .stripe-green{height:3px;background:var(--green)}
  .footer-bands .stripe-gap{height:1px;background:var(--paper)}
  .footer-bands .stripe-blue{height:5px;background:var(--blue)}

  .brand{display:flex;align-items:center;gap:4px}
  .brand-dot{border-radius:50%;background:var(--green);flex:none}
  .brand-name{font-weight:700;color:var(--green);white-space:nowrap;letter-spacing:.02em}
  .seal{position:absolute;border-radius:50%;background:var(--faint)}
  .contact{position:absolute;font-size:3.4px;line-height:1.45;color:var(--muted);white-space:nowrap}

  /* business cards */
  .card-front{left:20px;top:24px;width:125px;height:72px}
  .card-front .brand{position:absolute;left:8px;top:9px}
  .card-front .brand-dot{width:12px;height:12px}
  .card-front .brand-name{font-size:7px}
  .card-front .contact{left:8px;top:30px;font-size:4.2px}
  .card-caption{position:absolute;left:20px;top:104px;font-size:6px;color:#c9c9c9;letter-spacing:.04em}
  .card-white{left:20px;top:205px;width:120px;height:62px}
  .card-white .seal{left:6px;top:10px;width:30px;height:30px;background:var(--green)}
  .card-white .person{position:absolute;left:44px;top:14px;font-size:5.5px;font-weight:700;color:var(--blue)}
  .card-white .role{position:absolute;left:44px;top:22px;font-size:4px;color:var(--green)}
  .card-green{left:150px;top:205px;width:105px;height:62px;background:var(--green)}
  .card-green .seal{left:36px;top:14px;width:32px;height:32px;background:var(--green-light)}

  /* letterheads */
  .letterhead{top:18px;width:155px;height:205px}
  .letterhead.first{left:355px}
  .letterhead.second{left:528px}
  .letterhead .brand{position:absolute;left:10px;top:10px}
  .letterhead .brand-dot{width:9px;height:9px}
  .letterhead .brand-name{font-size:5.5px}
  .letterhead .contact{left:86px;top:10px}
  .letterhead .seal{left:45px;top:70px;width:65px;height:65px}

  /* envelope fronts */
  .envelope{left:700px;width:215px}
  .envelope.small{top:92px;height:60px}
  .envelope.large{top:178px;height:72px}
  .envelope .brand{position:absolute;left:9px;top:8px}
  .envelope .brand-dot{width:9px;height:9px}
  .envelope .brand-name{font-size:5.5px}
  .envelope .contact{left:22px;top:20px}

  /* envelope backs */
  .envelope-back{left:945px;width:222px;height:55px}
  .envelope-back.blue{top:98px}
  .envelope-back.green{top:160px}
  .envelope-back.white{top:222px}
  .envelope-back svg{position:absolute;inset:0;width:100%;height:100%}
  .envelope-back .brand{position:absolute;left:50%;top:40px;transform:translateX(-50%)}
  .envelope-back .brand-dot{width:8px;height:8px}
  .envelope-back .brand-name{font-size:5px}
</style>
</head>
<body>

<!-- business card front -->
<div class="piece card-front">
  <div class="brand"><span class="brand-dot"></span><span class="brand-name">Valcourt Chiropractic</span></div>
  <div class="contact">41785 Brookhaven Rd<br>Oakridge Twp, MI 48193<br>www.ValcourtChiroExample.com</div>
  <div class="footer-bands"><span class="stripe-green"></span><span class="stripe-gap"></span><span class="stripe-blue"></span></div>
</div>
<div class="card-caption">Business card · Letterhead · Envelope</div>

<div class="piece card-white">
  <div class="seal"></div>
  <div class="person">Dr. Valcourt</div>
  <div class="role">Doctor of Chiropractic</div>
  <div class="footer-bands"><span class="stripe-green"></span><span class="stripe-gap"></span><span class="stripe-blue"></span></div>
</div>

<div class="piece card-green">
  <div class="seal"></div>
</div>

<!-- letterheads -->
<div class="piece letterhead first">
  <div class="brand"><span class="brand-dot"></span><span class="brand-name">Valcourt Chiropractic</span></div>
  <div class="contact">41785 Brookhaven Rd<br>Oakridge Twp, MI 48193<br>info@ValcourtChiroExample.com<br>www.ValcourtChiroExample.com</div>
  <div class="seal"></div>
  <div class="footer-bands"><span class="stripe-green"></span><span class="stripe-gap"></span><span class="stripe-blue"></span></div>
</div>

<div class="piece letterhead second">
  <div class="brand"><span class="brand-dot"></span><span class="brand-name">Valcourt Chiropractic</span></div>
  <div class="contact">41785 Brookhaven Rd<br>Oakridge Twp, MI 48193<br>info@ValcourtChiroExample.com<br>www.ValcourtChiroExample.com</div>
  <div class="seal"></div>
  <div class="footer-bands"><span class="stripe-green"></span><span class="stripe-gap"></span><span class="stripe-blue"></span></div>
</div>

<!-- envelope fronts -->
<div class="piece envelope small">
  <div class="brand"><span class="brand-dot"></span><span class="brand-name">Valcourt Chiropractic</span></div>
  <div class="contact">41785 Brookhaven Rd<br>Oakridge Twp, MI 48193</div>
  <div class="footer-bands"><span class="stripe-green"></span><span class="stripe-gap"></span><span class="stripe-blue"></span></div>
</div>

<div class="piece envelope large">
  <div class="brand"><span class="brand-dot"></span><span class="brand-name">Valcourt Chiropractic</span></div>
  <div class="contact">41785 Brookhaven Rd<br>Oakridge Twp, MI 48193</div>
  <div class="footer-bands"><span class="stripe-green"></span><span class="stripe-gap"></span><span class="stripe-blue"></span></div>
</div>

<!-- envelope backs -->
<div class="piece envelope-back blue">
  <svg viewBox="0 0 100 25" preserveAspectRatio="none"><path d="M0 0 L100 0 L100 5 L50 14 L0 5Z" fill="var(--blue)"/><path d="M0 25 L50 12 L100 25" fill="none" stroke="var(--fold)" stroke-width=".3"/></svg>
</div>
<div class="piece envelope-back green">
  <svg viewBox="0 0 100 25" preserveAspectRatio="none"><path d="M0 0 L100 0 L100 5 L50 14 L0 5Z" fill="var(--green)"/><path d="M0 25 L50 12 L100 25" fill="none" stroke="var(--fold)" stroke-width=".3"/></svg>
  <div class="brand"><span class="brand-dot"></span><span class="brand-name">Valcourt Chiropractic</span></div>
</div>
<div class="piece envelope-back white">
  <svg viewBox="0 0 100 25" preserveAspectRatio="none"><path d="M0 0 L100 0 L100 5 L50 14 L0 5Z" fill="#f4f4f4" stroke="#d8d8d8" stroke-width=".3"/><path d="M0 25 L50 12 L100 25" fill="none" stroke="var(--fold)" stroke-width=".3"/></svg>
  <div class="brand"><span class="brand-dot"></span><span class="brand-name">Valcourt Chiropractic</span></div>
</div>

</body>
</html>
```